Small Machinery Hire Company Needs Coaster Design

Please design an eye catching coaster/sticker to place in local pubs and restaurants. Please use our attached logo and incorporate our rustic earthy feel into the colours. Use the following details. Definite want the focus to be on the logo and phone number.

Would appreciate if it could be multi-purpose as a basic sign as well.

Dry/Wet Hire Available
Ph: 0471629058

(Use FaceBook icon) kestrelpages.net/bramwellkestrelplant2917/

Target Market(s)

At homer DIY-ers. Middle class men who would like to hire a machine to work on their own pride and joy home.

Industry/Entity Type

Construction Company

Font styles to use
Other font styles liked:
• Something that matches the Logo

Colors
fefdec
ec1f27
474747
919191

Requirements
Nice to have
• Preferably a square shape so the it is more multi purpose

```html
<!DOCTYPE html>
<html lang="en">
<head>
<meta charset="utf-8">
<title>Bramwell Kestrel Plant – Coaster</title>
<link rel="stylesheet" href="https://fonts.googleapis.com/css2?family=Oswald:wght@500;700&family=Open+Sans:wght@400&display=swap">
<style>
  :root {
    --page: #ffffff;
    --coaster: #bdbbbc;
    --frame: #474747;
    --ink: #111111;
    --brand-red: #8a1518;
    --accent-red: #ec1f27;
    --muted: #333333;
  }
  html, body {
    margin: 0;
    padding: 0;
    width: 1200px;
    height: 758px;
    overflow: hidden;
    background: var(--page);
  }
  .canvas {
    position: relative;
    width: 1200px;
    height: 758px;
  }
  .coaster {
    position: absolute;
    left: 358px;
    top: 167px;
    width: 498px;
    height: 469px;
    box-sizing: border-box;
    border: 1.5px solid #1a1a1a;
    border-radius: 22px;
    background: var(--coaster);
  }
  .coaster-frame {
    position: absolute;
    left: 20px;
    top: 19px;
    width: 455px;
    height: 428px;
    box-sizing: border-box;
    border: 3px solid var(--frame);
    border-radius: 16px;
  }
  .brand-initials,
  .brand-full {
    position: absolute;
    left: 0;
    right: 0;
    margin: 0;
    text-align: center;
    font-family: "Oswald", sans-serif;
    font-weight: 700;
    color: var(--brand-red);
    text-transform: uppercase;
    line-height: 1;
  }
  .brand-initials {
    top: 36px;
    font-size: 185px;
    letter-spacing: 4px;
  }
  .brand-full {
    top: 235px;
    font-size: 35px;
    letter-spacing: 0;
  }
  .hire-note {
    position: absolute;
    left: 0;
    right: 0;
    top: 309px;
    margin: 0;
    text-align: center;
    font-family: "Oswald", sans-serif;
    font-weight: 500;
    font-size: 22px;
    color: var(--accent-red);
    text-transform: uppercase;
  }
  .phone {
    position: absolute;
    left: 0;
    right: 0;
    top: 342px;
    margin: 0;
    text-align: center;
    font-family: "Oswald", sans-serif;
    font-weight: 500;
    font-size: 23px;
    color: var(--ink);
    letter-spacing: 0.5px;
  }
  .social-row {
    position: absolute;
    left: 88px;
    top: 432px;
    display: flex;
    align-items: center;
    gap: 8px;
    padding: 0 8px;
    background: var(--coaster);
  }
  .social-mark {
    width: 24px;
    height: 24px;
    border-radius: 2px;
    background: var(--frame);
  }
  .social-url {
    font-family: "Open Sans", sans-serif;
    font-size: 16px;
    color: var(--muted);
  }
</style>
</head>
<body>
  <div class="canvas">
    <div class="coaster">
      <div class="coaster-frame"></div>
      <p class="brand-initials">BKP</p>
      <h1 class="brand-full">Bramwell Kestrel Plant</h1>
      <p class="hire-note">Dry/Wet Hire Available</p>
      <p class="phone">0471629058</p>
      <div class="social-row">
        <span class="social-mark"></span>
        <span class="social-url">kestrelpages.net/bramwellkestrelplant2917/</span>
      </div>
    </div>
  </div>
</body>
</html>
```